Refresh of The Marston Collective business card

Update business card design using existing primary logo. Names, numbers, etc. are too hard to read on current design.

Target Market(s)

We are a CPA firm.

Industry/Entity Type

Accountant

Contact Information for Business Card

update current card

Colors
0355a3
3176b5
85acd3
0792cd

Requirements
Must have
• Easier to read phone numbers and names
• Use existing logo
Nice to have
• We love our color scheme and current TMC logo. But the names and phone numbers are too small and card just look old and stale.

```html
<!DOCTYPE html>
<html lang="en">
<head>
<meta charset="utf-8">
<title>The Marston Collective – Business Card</title>
<link rel="stylesheet" href="https://fonts.googleapis.com/css2?family=Cinzel:wght@400;600&family=Questrial&display=swap">
<style>
  :root {
    --backdrop: #444548;
    --backdrop-dark: #2f3033;
    --card-dark: #232428;
    --card-front: #1d1e21;
    --emboss: #34363b;
    --brand-blue: #0355a3;
    --brand-mid: #3176b5;
    --brand-light: #85acd3;
    --brand-bright: #0792cd;
    --text-light: #f2f3f5;
    --text-grey: #a9acb2;
  }
  * { box-sizing: border-box; margin: 0; padding: 0; }
  html, body { width: 799px; height: 1200px; overflow: hidden; }
  body {
    background: radial-gradient(ellipse at 60% 40%, var(--backdrop), var(--backdrop-dark));
    font-family: "Questrial", sans-serif;
    position: relative;
  }
  .card {
    position: absolute;
    left: 90px;
    width: 620px;
    height: 354px;
    border-radius: 4px;
    overflow: hidden;
    box-shadow: 0 18px 40px rgba(0,0,0,.45);
  }
  .card--front { top: 120px; background: var(--card-front); }
  .card--back { top: 700px; background: var(--card-dark); }

  /* front */
  .front-mark {
    position: absolute;
    left: 50%; top: 50%;
    width: 170px; height: 170px;
    margin: -85px 0 0 -85px;
    border-radius: 50%;
    border: 3px solid var(--emboss);
    display: flex; align-items: center; justify-content: center;
    text-align: center;
  }
  .front-mark__name {
    font-family: "Cinzel", serif;
    font-weight: 600;
    font-size: 18px;
    line-height: 1.25;
    color: var(--emboss);
    width: 130px;
  }

  /* back */
  .back-art {
    position: absolute; inset: 0;
    background: linear-gradient(205deg, var(--brand-mid) 0%, var(--brand-blue) 34%, var(--card-dark) 66%);
  }
  .holder {
    position: absolute; right: 28px; top: 54px; text-align: right;
  }
  .holder__name {
    font-family: "Cinzel", serif;
    font-size: 22px;
    color: var(--text-light);
    letter-spacing: .5px;
  }
  .holder__title { font-size: 16px; color: var(--text-light); margin-top: 2px; }

  .brand {
    position: absolute; left: 28px; top: 118px;
    display: flex; align-items: center; gap: 14px;
  }
  .brand__dot {
    width: 66px; height: 66px; border-radius: 50%;
    background: var(--brand-blue);
  }
  .brand__name {
    font-family: "Cinzel", serif;
    font-weight: 600;
    font-size: 24px;
    line-height: 1.1;
    color: var(--brand-mid);
  }
  .brand__tagline {
    position: absolute; left: 108px; top: 194px;
    font-size: 9px; letter-spacing: 1.6px; text-transform: uppercase;
    color: var(--text-grey);
  }
  .address {
    position: absolute; left: 28px; top: 226px;
    font-size: 15px; line-height: 1.35; color: var(--text-grey);
    font-style: normal;
  }
  .contact {
    position: absolute; right: 24px; bottom: 22px;
    list-style: none; text-align: right;
    font-size: 16px; line-height: 1.35; color: var(--text-light);
  }
  .contact li { display: flex; justify-content: flex-end; align-items: center; gap: 10px; }
  .contact svg { width: 14px; height: 14px; fill: var(--brand-bright); }
</style>
</head>
<body>

<section class="card card--front" aria-label="Card front">
  <div class="front-mark">
    <span class="front-mark__name">The Marston Collective</span>
  </div>
</section>

<section class="card card--back" aria-label="Card back">
  <div class="back-art" role="img" aria-label="Decorative blue and silver wave band across the top of the card"></div>

  <div class="holder">
    <p class="holder__name">Daniel R. Marston, CPA</p>
    <p class="holder__title">President</p>
  </div>

  <div class="brand">
    <span class="brand__dot" aria-hidden="true"></span>
    <span class="brand__name">The Marston<br>Collective</span>
  </div>
  <p class="brand__tagline">Certified Public Accountants</p>

  <address class="address">
    312 Lakeview Ave. Suite 104<br>
    Winter Park, Florida 32789
  </address>

  <ul class="contact">
    <li>555.210.4381
      <svg viewBox="0 0 16 16" aria-label="Office"><path d="M2 5c0-2 2-3 6-3s6 1 6 3v1h-3V5H5v1H2z M4 7h8l2 7H2z"/></svg></li>
    <li>555.318.2704
      <svg viewBox="0 0 16 16" aria-label="Fax"><path d="M4 1h8v4H4z M1 6h14v7h-3v2H4v-2H1z M5 10v4h6v-4z"/></svg></li>
    <li>555.462.9157
      <svg viewBox="0 0 16 16" aria-label="Mobile"><path d="M4 0h8a1 1 0 0 1 1 1v14a1 1 0 0 1-1 1H4a1 1 0 0 1-1-1V1a1 1 0 0 1 1-1z M5 2v10h6V2z"/></svg></li>
    <li>dan@marstoncollective.com
      <svg viewBox="0 0 16 16" aria-label="Email"><path d="M0 3h16v10H0z M1 4l7 5 7-5" stroke="#232428" stroke-width="1"/></svg></li>
  </ul>
</section>

</body>
</html>
```